Kestrel Builders Business Card Design Project

Clean sharp business card
Ability to write on back of card
Details for the card -
Address: PO Box 5867, Tingapla, Qld, 4173
ABN: 47 305 961 220
BSA LIC 2650874
Ph: 07 3562 4470
Fax: 07 3562 4475
Email: kestrelbuilders@mailbrook.com.au

```html
<!DOCTYPE html>
<html lang="en">
<head>
<meta charset="utf-8">
<title>Kestrel Builders – Business Cards</title>
<link rel="stylesheet" href="https://fonts.googleapis.com/css2?family=Crimson+Text:wght@400;600&display=swap">
<style>
  :root {
    --page: #ffffff;
    --blue-bg: #d6e1f2;
    --blue-city: #8ba3d4;
    --blue-ink: #2e3a8c;
    --green-bg: #c5de8f;
    --green-city: #b3d46c;
    --green-ink: #1e6b3a;
    --name-ink: #5a5a5e;
    --accent: #f28a1e;
    --serif: "Crimson Text", Georgia, serif;
  }
  * { box-sizing: border-box; margin: 0; padding: 0; }
  html, body {
    width: 1036px;
    height: 1200px;
    overflow: hidden;
    background: var(--page);
  }
  .canvas {
    position: relative;
    width: 1036px;
    height: 1200px;
  }
  .card {
    position: absolute;
    left: 78px;
    width: 882px;
    height: 477px;
    overflow: hidden;
    font-family: var(--serif);
  }
  .card--blue { top: 70px; background: var(--blue-bg); --city: var(--blue-city); --ink: var(--blue-ink); }
  .card--green { top: 597px; background: var(--green-bg); --city: var(--green-city); --ink: var(--green-ink); }

  .skyline {
    position: absolute;
    inset: 0;
  }
  .skyline__towers {
    position: absolute;
    left: 279px;
    right: 0;
    top: 113px;
    bottom: 0;
    background: linear-gradient(to bottom, color-mix(in srgb, var(--city) 55%, transparent) 0%, var(--city) 45%);
  }
  .skyline__low {
    position: absolute;
    left: 0;
    width: 279px;
    top: 310px;
    bottom: 0;
    background: linear-gradient(to bottom, color-mix(in srgb, var(--city) 55%, transparent) 0%, var(--city) 50%);
  }
  .brand {
    position: absolute;
    left: 40px;
    top: 92px;
    display: flex;
    align-items: center;
    gap: 16px;
  }
  .brand__dot {
    width: 28px;
    height: 28px;
    border-radius: 50%;
    background: var(--accent);
  }
  .brand__name {
    font-family: var(--serif);
    font-weight: 600;
    font-size: 56px;
    line-height: 1;
    color: var(--name-ink);
    letter-spacing: 0.5px;
  }
  .details {
    position: absolute;
    left: 38px;
    top: 334px;
    list-style: none;
    color: var(--ink);
    font-size: 24px;
    line-height: 32.4px;
    text-shadow: 0 0 2px rgba(255,255,255,0.85);
    white-space: nowrap;
  }
</style>
</head>
<body>
<div class="canvas">
  <section class="card card--blue">
    <div class="skyline" role="img" aria-label="City skyline silhouette in soft blue">
      <div class="skyline__low"></div>
      <div class="skyline__towers"></div>
    </div>
    <div class="brand">
      <span class="brand__dot"></span>
      <span class="brand__name">Kestrel Builders</span>
    </div>
    <ul class="details">
      <li>ABN : 47 305 961 220</li>
      <li>BAS LIC : 2650874</li>
      <li>Address: PO Box 5867, Tingapla, Qld, 4173</li>
      <li>Phone: 35624470 • Fax: 35624475 • Email: kestrelbuilders@mailbrook.com.au</li>
    </ul>
  </section>

  <section class="card card--green">
    <div class="skyline" role="img" aria-label="City skyline silhouette in soft green">
      <div class="skyline__low"></div>
      <div class="skyline__towers"></div>
    </div>
    <div class="brand">
      <span class="brand__dot"></span>
      <span class="brand__name">Kestrel Builders</span>
    </div>
    <ul class="details">
      <li>ABN : 47 305 961 220</li>
      <li>BAS LIC : 2650874</li>
      <li>Address: PO Box 5867, Tingapla, Qld, 4173</li>
      <li>Phone: 35624470 • Fax: 35624475 • Email: kestrelbuilders@mailbrook.com.au</li>
    </ul>
  </section>
</div>
</body>
</html>
```